I need a cover for a brochure made

I need a cover for a brochure. The dimensions are 8.25 wide and 5.25 high... I also need a .25 inch bleed outside of those dimensions.

I need it to look like a vintage photo album cover. In big words, I would like it to say "Family". Above it in smaller words "To our Harlow Fairway" ... making it look like the words are gold inlay or something.

I would like it kind of in the style of some of the attached maybe. Just vintage looking.

```html
<!DOCTYPE html>
<html lang="en">
<head>
<meta charset="utf-8">
<title>Family – Brochure Cover</title>
<link rel="stylesheet" href="https://fonts.googleapis.com/css2?family=Abril+Fatface&display=swap">
<style>
  :root {
    --cover-brown: #382c2b;
    --inlay-gold: #d4ae3a;
    --ornament-glow: rgba(212, 174, 58, 0.55);
    --ornament-fade: rgba(212, 174, 58, 0.08);
  }
  html, body {
    margin: 0;
    padding: 0;
    width: 1200px;
    height: 796px;
    overflow: hidden;
    background: var(--cover-brown);
  }
  .cover {
    position: relative;
    width: 1200px;
    height: 796px;
    background: var(--cover-brown);
    overflow: hidden;
    font-family: "Abril Fatface", Georgia, serif;
    color: var(--inlay-gold);
  }
  .frame-rule {
    position: absolute;
    background: var(--inlay-gold);
  }
  .frame-rule--top    { left: 302px; top: 27px;  width: 597px; height: 9px; }
  .frame-rule--bottom { left: 302px; top: 760px; width: 597px; height: 9px; }
  .frame-rule--left   { left: 31px;  top: 308px; width: 8px;   height: 180px; }
  .frame-rule--right  { left: 1161px; top: 308px; width: 8px;  height: 180px; }

  .corner-ornament {
    position: absolute;
    width: 259px;
    height: 274px;
  }
  .corner-ornament--tl { left: 19px;  top: 18px;
    background: radial-gradient(ellipse at 0% 0%, var(--ornament-glow), var(--ornament-fade) 70%, transparent 90%); }
  .corner-ornament--tr { left: 922px; top: 18px;
    background: radial-gradient(ellipse at 100% 0%, var(--ornament-glow), var(--ornament-fade) 70%, transparent 90%); }
  .corner-ornament--bl { left: 19px;  top: 505px;
    background: radial-gradient(ellipse at 0% 100%, var(--ornament-glow), var(--ornament-fade) 70%, transparent 90%); }
  .corner-ornament--br { left: 922px; top: 505px;
    background: radial-gradient(ellipse at 100% 100%, var(--ornament-glow), var(--ornament-fade) 70%, transparent 90%); }

  .cover-title {
    position: absolute;
    left: 250px;
    top: 205px;
    width: 690px;
    margin: 0;
    text-align: center;
    font-weight: 400;
    font-size: 212px;
    line-height: 1;
    transform: rotate(-3deg);
    transform-origin: center;
  }
  .title-underline {
    position: absolute;
    left: 310px;
    top: 430px;
    width: 482px;
    height: 10px;
    background: var(--inlay-gold);
    transform: rotate(-3.2deg);
    transform-origin: center;
  }
  .cover-dedication {
    position: absolute;
    left: 290px;
    top: 462px;
    width: 640px;
    margin: 0;
    text-align: center;
    font-weight: 400;
    font-size: 54px;
    line-height: 1.2;
    transform: rotate(-2deg);
    transform-origin: center;
  }
</style>
</head>
<body>
  <main class="cover">
    <div class="frame-rule frame-rule--top"></div>
    <div class="frame-rule frame-rule--bottom"></div>
    <div class="frame-rule frame-rule--left"></div>
    <div class="frame-rule frame-rule--right"></div>

    <div class="corner-ornament corner-ornament--tl" role="img" aria-label="Gold vintage floral scroll ornament, top left corner"></div>
    <div class="corner-ornament corner-ornament--tr" role="img" aria-label="Gold vintage floral scroll ornament, top right corner"></div>
    <div class="corner-ornament corner-ornament--bl" role="img" aria-label="Gold vintage floral scroll ornament, bottom left corner"></div>
    <div class="corner-ornament corner-ornament--br" role="img" aria-label="Gold vintage floral scroll ornament, bottom right corner"></div>

    <h1 class="cover-title">Family</h1>
    <div class="title-underline"></div>
    <p class="cover-dedication">To our Harlow Fairway</p>
  </main>
</body>
</html>
```